【お店の名前】
山形県にあるインド料理レストラン花野ポルカナです。
あまり英語が得意でないインド人が命名し、スター☆を付けたかったのが、インド英語になり、
ポルカナとなってしまっております。

山形県東根市は自然、、野菜、果物がおおくとれる、とても自然豊かな場所です。
メニューのカレーには我が家の畑でつくっている自家製野菜をつかっています。

派手な看板から、女性やカップルのからもはいりにくい外観で、何の店かわからない状態でしたので、
誰がみてもカレーのインド料理屋さんとわかるデザインにおねがいしたいです。

【カフェのコンセプト】
●基本コンセプト:
地元野菜をつかったインド料理を、ファミリー、カップル、女性1人でも安心して気軽に楽しめ、穏やかな時間が過ごせるレストラン
(エスニックのインドらしさを残しながら、インドインドしすぎないデザイン)

●提供するもの:
新鮮な食材を使った手作りのインド料理をリーズナブルな価格にて提供。

●想定するお客様:
子供さんから大人まで来店されていますが、1番はファミリー層

●店舗イメージ:
いまから外壁のペンキ塗り直し予定ですが、外壁はクリーム色で屋根は濃赤です。

●大切にしたいこと:
お客様の身近である、地元野菜をつかっているということ、お米も山形県産
今までインド料理を食べたことがない人も、気軽に「あ、おいしそう、いってみようかな」と思えるレストラン

【依頼する看板への記載要望】
<文字>
●真ん中に:メインの店名は、「インド料理レストラン花野ポルカナ(日本語)Hanano Polkana(英語)」の2パターン
・左上に:「地元野菜をつかったインドカレー&もちもちナン」→真ん中の店名より小さめの文字で書いてください。
真ん中の文字が100なら60とかのパランスでお願いします。
・お持ち帰りOK Takeout ok→なにか吹き出しのなかに入れてください。
吹き出しの形は問いませんが、派手な吹き出しでなく、シンプルな〇のような形がいいです
<デザイン>
・野菜のイラストとスパイス、ロゴ、バターチキンカレー、ナン、を組み合わせた看板としたいです。
野菜はトマト、玉ねぎ、ほうれん草、ナス、スパイスは赤唐辛子、などのインドのスパイスを4,5個を希望します。
(バランスはナンを大きく、さりげなく野菜とスパイス、ロゴを入れてください)
●背景の色はインドの旗の色をつかって3色で使ってほしいです。(看板全体に)
赤系、黄・オレンジ系、緑系
【その他】
●他社で商標登録してあるものの盗用、転用は無しとして下さい。また、選択させて頂いたロゴの著作権(財産権)等の扱いはQuilliant利用規約に従い、当方に譲渡をお願いします。

以上、私の想いをいろいろと記載しましたが、纏めますとイメージ&キーワードは以下通りです。

安心、暖かみ、清潔、ほんのりエスニック、地元野菜

皆様の自由な発想とご提案を心から楽しみにしております。
なにとぞ宜しくお願いいたします。
ロゴを添付いたします。
よろしくお願い申し上げます。

うまくできた場合引き続きお願いする場合があります。
スピード重視でいいデザインがあった場合締め切らせていただく場合が御座います。
正面 よこ6300 高さ1825
南側 よこw2500 高さ810

看板大きさになります!
正面の看板と、南側の看板の2種類となりますので、そのサイズ用で2種類お願いしたくぞんじます!
デザインはおなじです!
早速のご提案してくださった皆様ありがとうございます!

長文で分かりづらい部分があるかと思いますので追記します。
1.店名は日本語と英語の2パターンで、2行にわけてください。

2野菜のイラストとスパイス、ロゴ→こちらはイラストで
バターチキンカレー、ナン→こちらは写真を組み合わせた看板としたいです。
スパイスのイメージイラスト添付します!

すばやいご対応と、イメージ通りのデザインでした(^_^)応募してくださりました皆様、大変ありがとうございました!

ほかにも看板募集しますので、また色々応募いただけますと嬉しいです♩
応募してくださりましてありがとうございました!

```html
<!DOCTYPE html>
<html lang="ja">
<head>
<meta charset="utf-8">
<title>花野ポルカナ 看板デザイン案</title>
<link href="https://fonts.googleapis.com/css2?family=Noto+Sans+JP:wght@500;700;900&family=Dancing+Script:wght@700&display=swap" rel="stylesheet">
<style>
  :root{
    --paper:#ffffff;
    --ink:#333333;
    --cream:#fff6d6;
    --yellow:#fbd55a;
    --orange:#f2a132;
    --red:#c8321e;
    --brown:#5a2a14;
    --green:#3f8f3a;
    --green-light:#8cc26a;
    --naan:#e9cf9c;
    --curry:#d9822b;
    --stamp:#e07a8c;
    --photo:#8d8f8a;
  }
  *{box-sizing:border-box;margin:0;padding:0}
  html,body{width:863px;height:1200px;overflow:hidden;background:var(--paper)}
  body{font-family:"Noto Sans JP",sans-serif;color:var(--ink);position:relative}

  .sheet-label{position:absolute;left:115px;font-size:12px;font-weight:500}

  .signboard{position:absolute;left:115px;width:656px;container-type:inline-size;overflow:hidden;
    background:linear-gradient(180deg,var(--cream) 0%,var(--yellow) 100%);border:1px solid #ddd}
  .signboard--front{top:40px;height:190px}
  .signboard--south{top:345px;height:212px}

  .bg-corner{position:absolute;left:0;top:0;width:40%;height:100%;
    background:linear-gradient(160deg,var(--orange) 0%,transparent 45%)}
  .bg-base{position:absolute;left:0;bottom:0;width:100%;height:8%;background:var(--green)}
  .bg-top{position:absolute;left:0;top:0;width:100%;height:4%;background:var(--red)}

  .photo-curry{position:absolute;left:-3%;top:45%;width:27%;height:66%;border-radius:50%;
    background:radial-gradient(circle at 50% 40%,var(--curry),#a8521a)}
  .photo-naan{position:absolute;right:0;top:0;width:34%;height:100%;
    background:radial-gradient(ellipse at 40% 50%,#f5e2b8,var(--naan) 60%,#c79a58)}

  .spice{position:absolute;width:2.4cqw;height:2.4cqw;border-radius:50%}
  .spice--a{left:34%;top:9%;background:var(--green-light)}
  .spice--b{left:60%;top:7%;background:var(--red)}
  .spice--c{left:46%;top:82%;background:var(--orange)}

  .tagline{position:absolute;left:4%;top:11%;width:29%;padding:.9cqw 1cqw;background:var(--red);
    color:#fff;font-weight:700;font-size:1.9cqw;line-height:1.4;border-radius:.6cqw;text-align:center;white-space:nowrap}

  .takeout{position:absolute;top:58%;width:7cqw;height:7cqw;border-radius:50%;background:var(--green);
    color:#fff;font-weight:700;font-size:1.2cqw;line-height:1.2;display:flex;align-items:center;justify-content:center;text-align:center}
  .takeout--jp{left:25%}
  .takeout--en{left:33%}

  .genre{position:absolute;left:32%;top:22%;color:var(--brown);font-weight:900;font-size:3cqw;line-height:1.2;white-space:nowrap}
  .shop-name{position:absolute;left:48.5%;top:19%;color:var(--brown);font-weight:900;font-size:6cqw;line-height:1.1;white-space:nowrap}
  .shop-name-en{position:absolute;left:50%;top:58%;color:var(--brown);font-family:"Dancing Script",cursive;font-size:3.8cqw;line-height:1.2;white-space:nowrap}

  .brand-mark{position:absolute;right:2%;top:8%;width:9.5cqw;height:9.5cqw;border-radius:50%;border:.3cqw solid var(--stamp);
    background:#fff;display:flex;align-items:center;justify-content:center;color:var(--stamp);font-weight:700;font-size:1.2cqw;line-height:1.3;text-align:center}

  .install-photo{position:absolute;left:115px;top:630px;width:656px;height:505px;
    background:linear-gradient(180deg,#cfd8e0 0%,#b9b3a4 45%,var(--photo) 100%)}
</style>
</head>
<body>
  <p class="sheet-label" style="top:20px">正面</p>
  <section class="signboard signboard--front">
    <div class="bg-corner"></div><div class="bg-top"></div><div class="bg-base"></div>
    <div class="photo-curry" role="img" aria-label="バターチキンカレーの写真"></div>
    <div class="photo-naan" role="img" aria-label="焼きたてナンの写真"></div>
    <div class="spice spice--a" role="img" aria-label="ほうれん草のイラスト"></div>
    <div class="spice spice--b" role="img" aria-label="赤唐辛子のイラスト"></div>
    <div class="spice spice--c" role="img" aria-label="スパイスのイラスト"></div>
    <p class="tagline">地元野菜をつかった<br>インドカレー&amp;もちもちナン</p>
    <p class="takeout takeout--jp">お持ち帰り<br>OK</p>
    <p class="takeout takeout--en">Takeout<br>OK</p>
    <p class="genre">インド料理<br>レストラン</p>
    <h1 class="shop-name">花野ポルカナ</h1>
    <p class="shop-name-en">Hanano Polkana</p>
    <div class="brand-mark">花野<br>ポルカナ</div>
  </section>

  <p class="sheet-label" style="top:325px">南側</p>
  <section class="signboard signboard--south">
    <div class="bg-corner"></div><div class="bg-top"></div><div class="bg-base"></div>
    <div class="photo-curry" role="img" aria-label="バターチキンカレーの写真"></div>
    <div class="photo-naan" role="img" aria-label="焼きたてナンの写真"></div>
    <div class="spice spice--a" role="img" aria-label="ほうれん草のイラスト"></div>
    <div class="spice spice--b" role="img" aria-label="赤唐辛子のイラスト"></div>
    <div class="spice spice--c" role="img" aria-label="スパイスのイラスト"></div>
    <p class="tagline">地元野菜をつかった<br>インドカレー&amp;もちもちナン</p>
    <p class="takeout takeout--jp">お持ち帰り<br>OK</p>
    <p class="takeout takeout--en">Takeout<br>OK</p>
    <p class="genre">インド料理<br>レストラン</p>
    <p class="shop-name">花野ポルカナ</p>
    <p class="shop-name-en">Hanano Polkana</p>
    <div class="brand-mark">花野<br>ポルカナ</div>
  </section>

  <p class="sheet-label" style="top:610px">設置イメージ図</p>
  <div class="install-photo" role="img" aria-label="看板を取り付けた店舗外観の設置イメージ写真"></div>
</body>
</html>
```